RWT Installations Ltd Business Cards

We need a business card with our business logo. We provide window and door installations on high-rises in west coast British Colombia, Canada.

I would like my business information and details on one side of the card, and the other side the company name with logo

Target Market(s)

General Contractors

Industry/Entity Type

Construction

Contact Information for Business Card

one side i want my company name and logo in the dark theme logo that i provided

Requirements
Must have
• Tomas Verelund, 15559284016, RWTInstallations@mailvera.example, 1408-5192 Pellow Avenue Burnaby BC, V0X 1Z9, Owner & Manager

```html
<!DOCTYPE html>
<html lang="en">
<head>
<meta charset="utf-8">
<title>RWT Installations Ltd – Business Card</title>
<link href="https://fonts.googleapis.com/css2?family=Montserrat:wght@500;600;700&display=swap" rel="stylesheet">
<style>
  :root {
    --bg: #e9e7e5;
    --card-white: #ffffff;
    --card-black: #161616;
    --pattern-dark: #1e1e1e;
    --pattern-light: #5a5a5a;
    --brand-blue: #2aa0dc;
    --brand-grey: #8a8a8a;
    --ink: #1d1d1d;
  }
  * { box-sizing: border-box; margin: 0; padding: 0; }
  html, body { width: 1200px; height: 786px; overflow: hidden; }
  body {
    background: var(--bg);
    font-family: "Montserrat", sans-serif;
    color: var(--ink);
    position: relative;
  }
  .card {
    position: absolute;
    top: 238px;
    width: 540px;
    height: 309px;
    border-radius: 3px;
    box-shadow: 0 6px 18px rgba(0,0,0,.18);
    overflow: hidden;
  }
  .card--front { left: 40px; background: var(--card-white); }
  .card--back { left: 620px; background: var(--card-black); }

  .brand {
    position: absolute;
    display: flex;
    align-items: center;
    gap: 10px;
    font-weight: 600;
    color: var(--brand-blue);
    white-space: nowrap;
  }
  .brand__mark { width: 30px; height: 30px; background: var(--brand-grey); }
  .card--front .brand { left: 246px; top: 60px; font-size: 21px; }

  .rule { position: absolute; height: 1.5px; background: var(--brand-blue); }
  .rule--long { left: 250px; right: 40px; top: 122px; }
  .rule--short { left: 44px; width: 170px; top: 218px; }

  .person { position: absolute; left: 44px; top: 164px; }
  .person__name { font-size: 21px; font-weight: 700; color: var(--brand-blue); }
  .person__role { font-size: 12.5px; font-weight: 500; margin-top: 3px; }

  .address {
    position: absolute; right: 40px; top: 150px;
    font-size: 12.5px; font-weight: 500; line-height: 1.4; text-align: left;
  }

  .contacts { position: absolute; left: 44px; top: 234px; list-style: none; }
  .contacts li {
    display: flex; align-items: center; gap: 12px;
    font-size: 12.5px; font-weight: 500; height: 24px;
  }
  .contacts svg { width: 15px; height: 15px; fill: var(--brand-blue); flex: none; }

  .back-pattern {
    position: absolute; inset: 0;
    background: linear-gradient(120deg, var(--pattern-light) 0%, var(--pattern-dark) 45%, var(--card-black) 100%);
  }
  .card--back .brand {
    left: 50%; top: 50%; transform: translate(-50%, -50%);
    font-size: 22px;
  }
</style>
</head>
<body>
  <section class="card card--front">
    <div class="brand"><span class="brand__mark"></span>RWT Installations Ltd</div>
    <div class="rule rule--long"></div>

    <div class="person">
      <p class="person__name">Tomas Verelund</p>
      <p class="person__role">Owner &amp; Manager</p>
    </div>
    <div class="rule rule--short"></div>

    <p class="address">1408-5192 Pellow Avenue<br>Burnaby BC, V0X 1Z9</p>

    <ul class="contacts">
      <li>
        <svg viewBox="0 0 24 24" aria-hidden="true"><path d="M6.6 10.8a15.1 15.1 0 0 0 6.6 6.6l2.2-2.2a1 1 0 0 1 1-.25 11.4 11.4 0 0 0 3.6.57 1 1 0 0 1 1 1V20a1 1 0 0 1-1 1A17 17 0 0 1 3 4a1 1 0 0 1 1-1h3.5a1 1 0 0 1 1 1c0 1.25.2 2.45.57 3.6a1 1 0 0 1-.25 1z"/></svg>
        15559284016
      </li>
      <li>
        <svg viewBox="0 0 24 24" aria-hidden="true"><path d="M2 5h20v14H2z M2 5l10 8 10-8" /></svg>
        RWTInstallations@mailvera.example
      </li>
    </ul>
  </section>

  <section class="card card--back">
    <div class="back-pattern" role="img" aria-label="Repeating embossed pattern of building shapes on a black background"></div>
    <div class="brand"><span class="brand__mark"></span>RWT Installations Ltd</div>
  </section>
</body>
</html>
```